Medical Oncologist in Rural Australia needs a Business Card

I am a medical oncologist in a regional town in Australia. I need a business card that merges a degree of conservatism (as people's lives are entrusted to me) with cutting edge (as I am always trying to understand the latest cancer biology and trying to bring new drugs to patients rapidly). I wish my card to project the idea that I am trustworthy, caring and innovative. Not overly bold colours but something that doesn't drift into the background.

Medical

```html
<!DOCTYPE html>
<html lang="en">
<head>
<meta charset="utf-8">
<title>Riverbend Medical Oncology – Business Card</title>
<link rel="stylesheet" href="https://fonts.googleapis.com/css2?family=Marcellus&family=Open+Sans:wght@400;600&display=swap">
<style>
  :root {
    --page-bg: #ebe7e1;
    --navy: #2a2f6e;
    --indigo-deep: #34387f;
    --indigo-soft: #8c90cc;
    --sky: #5b9bd5;
    --ink-light: #5a86c4;
    --white: #ffffff;
  }
  * { box-sizing: border-box; margin: 0; padding: 0; }
  html, body {
    width: 1200px;
    height: 784px;
    overflow: hidden;
    background: var(--page-bg);
  }
  .canvas {
    position: relative;
    width: 1200px;
    height: 784px;
  }
  .card {
    position: absolute;
    top: 236px;
    width: 520px;
    height: 300px;
    border-radius: 4px;
    box-shadow: 0 8px 24px rgba(40, 36, 30, 0.18);
    overflow: hidden;
  }
  /* Back side */
  .card-back { left: 50px; }
  .card-back .pattern-field {
    position: absolute;
    inset: 0;
    background: radial-gradient(ellipse at 78% 45%, var(--indigo-soft) 0%, #6e72b6 38%, var(--indigo-deep) 78%);
  }
  .card-back .brand {
    position: absolute;
    left: 0; right: 0;
    top: 112px;
    display: flex;
    align-items: center;
    justify-content: center;
    gap: 14px;
    color: var(--white);
    font-family: "Marcellus", serif;
  }
  .brand-dot {
    width: 46px; height: 46px;
    border-radius: 50%;
    background: var(--white);
    flex: none;
  }
  .brand-name { line-height: 1.05; }
  .brand-name .line-main { display: block; font-size: 40px; }
  .brand-name .line-sub { display: block; font-size: 22px; letter-spacing: 3px; }

  /* Front side */
  .card-front { left: 630px; background: var(--white); }
  .card-front .brand {
    position: absolute;
    left: 36px; top: 40px;
    display: flex;
    align-items: center;
    gap: 14px;
    color: var(--navy);
    font-family: "Marcellus", serif;
  }
  .card-front .brand-dot { background: var(--sky); }
  .person {
    position: absolute;
    left: 40px; top: 170px;
    font-family: "Open Sans", sans-serif;
  }
  .person-name { font-size: 19px; font-weight: 600; color: var(--navy); }
  .person-credentials { font-size: 10px; color: var(--ink-light); margin-top: 1px; }
  .contact-list {
    position: absolute;
    left: 40px; top: 226px;
    list-style: none;
    font-family: "Open Sans", sans-serif;
    font-size: 12.5px;
    color: var(--navy);
  }
  .contact-list li {
    display: flex;
    align-items: center;
    gap: 7px;
    height: 17px;
  }
  .contact-icon { width: 12px; height: 12px; flex: none; fill: var(--ink-light); }
</style>
</head>
<body>
<main class="canvas">

  <section class="card card-back" aria-label="Card back">
    <div class="pattern-field" role="img" aria-label="Soft indigo field of overlapping translucent dots in perspective"></div>
    <div class="brand">
      <span class="brand-dot"></span>
      <span class="brand-name">
        <span class="line-main">Riverbend</span>
        <span class="line-sub">Medical Oncology</span>
      </span>
    </div>
  </section>

  <section class="card card-front" aria-label="Card front">
    <div class="brand">
      <span class="brand-dot"></span>
      <span class="brand-name">
        <span class="line-main">Riverbend</span>
        <span class="line-sub">Medical Oncology</span>
      </span>
    </div>

    <div class="person">
      <p class="person-name">Daniel Marsh</p>
      <p class="person-credentials">MBBS (hons), FRACP, BE (hons)</p>
    </div>

    <ul class="contact-list">
      <li>
        <svg class="contact-icon" viewBox="0 0 24 24" aria-hidden="true"><path d="M6.6 10.8a15.1 15.1 0 0 0 6.6 6.6l2.2-2.2a1 1 0 0 1 1-.25 11.4 11.4 0 0 0 3.6.57 1 1 0 0 1 1 1V20a1 1 0 0 1-1 1A17 17 0 0 1 3 4a1 1 0 0 1 1-1h3.5a1 1 0 0 1 1 1c0 1.25.2 2.45.57 3.57a1 1 0 0 1-.25 1z"/></svg>
        555-214-3097
      </li>
      <li>
        <svg class="contact-icon" viewBox="0 0 24 24" aria-hidden="true"><path d="M12 2a10 10 0 1 0 0 20 10 10 0 0 0 0-20zm6.9 6h-3a15 15 0 0 0-1.3-3.9A8 8 0 0 1 18.9 8zM12 4c.8 1.1 1.5 2.5 1.9 4h-3.8c.4-1.5 1.1-2.9 1.9-4zM4.3 14a8 8 0 0 1 0-4h3.4a16 16 0 0 0 0 4zm.8 2h3a15 15 0 0 0 1.3 3.9A8 8 0 0 1 5.1 16zm3-8h-3a8 8 0 0 1 4.3-3.9A15 15 0 0 0 8.1 8zM12 20c-.8-1.1-1.5-2.5-1.9-4h3.8c-.4 1.5-1.1 2.9-1.9 4zm2.3-6H9.7a14 14 0 0 1 0-4h4.6a14 14 0 0 1 0 4zm.3 5.9a15 15 0 0 0 1.3-3.9h3a8 8 0 0 1-4.3 3.9zm1.7-5.9a16 16 0 0 0 0-4h3.4a8 8 0 0 1 0 4z"/></svg>
        www.riverbendonc.com
      </li>
      <li>
        <svg class="contact-icon" viewBox="0 0 24 24" aria-hidden="true"><path d="M2 5h20v14H2zm2 2v.5l8 5 8-5V7zm0 2.8V17h16V9.8l-8 5z"/></svg>
        info@riverbendonc.com
      </li>
      <li>
        <svg class="contact-icon" viewBox="0 0 24 24" aria-hidden="true"><path d="M12 3 2 12h3v8h5v-6h4v6h5v-8h3z"/></svg>
        142 Carrington Road Dubbo
      </li>
    </ul>
  </section>

</main>
</body>
</html>
```